Stationary for a Legal Support Company
Brimvale Courier & Records, Inc.
Stationary for a Legal Support Company - Marketing
Creative Brief
Professional
Rupert J Olwen
PO Box 712 4175 Marrow Ln Fernmoor OH 40512
tkorvel@brimcr.com
www.brimcr.com
Generic USB flash and CD/DVD layout also appreciated.
Back of the card can include the logo or logo/text.
tkorvel tkorvel
Thank you all for your submissions. I believe I have sent some comments to everyone who has entered a submission. If you did not receive a comment from me, please let me know.

```html
<!DOCTYPE html>
<html lang="en">
<head>
<meta charset="utf-8">
<title>Brimvale Courier &amp; Records – Stationery Set</title>
<link href="https://fonts.googleapis.com/css2?family=Lato:wght@400;700&display=swap" rel="stylesheet">
<style>
:root{
  --bg:#868686;
  --paper:#ffffff;
  --navy:#23449a;
  --navy-dark:#1b3680;
  --ink:#3a4a7a;
  --hole:#dcdcdc;
  --faint:rgba(35,68,154,0.12);
  --faint-light:rgba(255,255,255,0.14);
}
*{margin:0;padding:0;box-sizing:border-box}
html,body{width:1200px;height:286px;overflow:hidden;background:var(--bg);font-family:'Lato',sans-serif}
.set{position:relative;width:1200px;height:286px}
.item{position:absolute;box-shadow:0 1px 3px rgba(0,0,0,.35)}
.paper{background:var(--paper)}
.blue{background:var(--navy)}
.brand{display:flex;align-items:center;gap:3px;color:var(--navy);font-weight:700;white-space:nowrap;line-height:1}
.brand .dot{width:6px;height:6px;border-radius:50%;background:currentColor;flex:none}
.on-blue .brand{color:#fff}
.tiny{font-size:3.2px;font-weight:400;color:var(--ink);line-height:1.35;white-space:nowrap}
.watermark{position:absolute;left:50%;top:50%;transform:translate(-50%,-50%);font-weight:700;white-space:nowrap;color:var(--faint)}
.watermark.light{color:var(--faint-light)}

/* business cards */
.card{width:62px;height:31px}
.card .brand{position:absolute;left:5px;top:6px;font-size:4.5px}
.card .brand .dot{width:4px;height:4px}
.card .tiny{position:absolute;left:5px;bottom:4px}
.card.back{display:flex;align-items:center;justify-content:center}
.card.back .brand{position:static;font-size:5px}
.card.wide{width:96px;height:38px}

/* letterhead */
.letter{width:148px;height:214px}
.letter .brand{position:absolute;left:12px;top:12px;font-size:6px}
.letter .tiny{position:absolute;left:12px;top:22px}
.letter .watermark{font-size:20px}
.letter .foot{position:absolute;left:12px;right:12px;bottom:10px;height:1px;background:var(--navy)}

/* envelope */
.envelope{width:168px;height:106px;overflow:hidden}
.envelope .flap{position:absolute;left:0;bottom:0;width:100%;height:48px}
.envelope .brand{position:absolute;left:8px;top:8px;font-size:5px}
.envelope .tiny{position:absolute;left:8px;top:16px}

/* folder */
.folder{width:362px;height:214px;display:flex}
.folder .panel{position:relative;height:100%}
.folder .left{width:172px}
.folder .right{width:190px}
.folder .right .brand{position:absolute;left:24px;top:64px;font-size:11px}
.folder .right .brand .dot{width:12px;height:12px}
.folder .left .watermark{font-size:28px}
.folder .pocket{position:absolute;left:0;bottom:0}

/* cd */
.cd{left:1007px;top:54px;width:84px;height:84px;border-radius:50%}
.cd .brand{position:absolute;left:14px;top:26px;font-size:5px}
.cd .brand .dot{width:4px;height:4px}
.cd .hole{position:absolute;left:36px;top:36px;width:12px;height:12px;border-radius:50%;background:var(--bg);box-shadow:inset 0 0 0 3px var(--hole)}
.sleeve{width:192px;height:101px;display:flex}
.sleeve .half{position:relative;width:50%;height:100%}
.sleeve .brand{position:absolute;left:14px;top:40px;font-size:7px}
.sleeve .tiny{position:absolute;left:14px;top:52px}
</style>
</head>
<body>
<main class="set">

  <div class="item paper card" style="left:19px;top:178px">
    <div class="brand"><span class="dot"></span>Brimvale</div>
    <div class="tiny">Rupert J Olwen<br>tkorvel@brimcr.com</div>
  </div>
  <div class="item paper card" style="left:87px;top:178px">
    <div class="brand"><span class="dot"></span>Brimvale</div>
    <div class="tiny">Rupert J Olwen<br>www.brimcr.com</div>
  </div>
  <div class="item blue card back on-blue" style="left:19px;top:213px"><div class="brand"><span class="dot"></span>Brimvale</div></div>
  <div class="item blue card back on-blue" style="left:87px;top:213px"><div class="brand"><span class="dot"></span>Brimvale</div></div>

  <div class="item paper letter" style="left:173px;top:48px">
    <div class="brand"><span class="dot"></span>Brimvale</div>
    <div class="tiny">Brimvale Courier &amp; Records, Inc.<br>PO Box 712 4175 Marrow Ln Fernmoor OH 40512</div>
    <div class="watermark">Brimvale</div>
    <div class="foot"></div>
  </div>
  <div class="item paper letter" style="left:336px;top:48px">
    <div class="brand"><span class="dot"></span>Brimvale</div>
    <div class="tiny">www.brimcr.com<br>tkorvel@brimcr.com</div>
    <div class="watermark">Brimvale</div>
    <div class="foot"></div>
  </div>

  <div class="item paper card wide" style="left:499px;top:101px">
    <div class="brand"><span class="dot"></span>Brimvale</div>
    <div class="tiny">Rupert J Olwen · tkorvel@brimcr.com<br>PO Box 712 4175 Marrow Ln Fernmoor OH 40512</div>
  </div>

  <div class="item paper envelope" style="left:475px;top:158px">
    <div class="brand"><span class="dot"></span>Brimvale</div>
    <div class="tiny">PO Box 712 4175 Marrow Ln<br>Fernmoor OH 40512</div>
    <svg class="flap" viewBox="0 0 168 48" preserveAspectRatio="none">
      <path d="M0 0 H168 V48 H0 Z" fill="#23449a"/>
      <path d="M0 0 L84 30 L168 0" fill="none" stroke="#ffffff" stroke-width="1.2"/>
    </svg>
  </div>

  <div class="item folder" style="left:648px;top:48px">
    <div class="panel left blue"><div class="watermark light">Brimvale</div></div>
    <div class="panel right paper">
      <div class="brand"><span class="dot"></span>Brimvale</div>
      <svg class="pocket" width="190" height="70" viewBox="0 0 190 70">
        <path d="M0 20 C60 20 80 0 130 0 H190 V70 H0 Z" fill="#1b3680"/>
      </svg>
    </div>
  </div>

  <div class="item paper cd">
    <div class="brand"><span class="dot"></span>Brimvale</div>
    <div class="hole"></div>
  </div>

  <div class="item sleeve" style="left:989px;top:163px">
    <div class="half paper">
      <div class="brand"><span class="dot"></span>Brimvale</div>
      <div class="tiny">Brimvale Courier &amp; Records, Inc.<br>www.brimcr.com</div>
    </div>
    <div class="half blue"></div>
  </div>

</main>
</body>
</html>
```